Belford & Company

We are a boutique commercial real estate firm. For our Business card design - sleek, modern, yet high-end/classy. Please see our website: belfordandcompany.example for details.

We currently need 2 business card names and the ability to add/change the business card information -
Name, Title, Address, Office #, Mobile #, Fax, Email and company website.

Industry/Entity Type

Real Estate

Contact Information for Business Card

Business card design - sleek, modern, yet high-end/classy. Please see our website: belfordandcompany.example for details.

Also, we'd like to have our slogan "Precision Guides Every Step." somewhere in there. We'd like to make some part of it raised or a different texture if possible.
Color #'s:
blue 19 36 128
light gray 222 222 221
dark gray 107 120 128

Also, we'd like to have our slogan "Precision Guides Every Step." somewhere in there. We'd like to make some part of it raised or a different texture if possible - grey on one side and blue on the other - rounded edges preferred. Maybe either metal/silver/grey raised logo on the back. Thank you!!

Requirements
Must have
• Sleek, modern, clean and classy design

```html
<!DOCTYPE html>
<html lang="en">
<head>
<meta charset="utf-8">
<title>Belford & Company – Business Card</title>
<link rel="stylesheet" href="https://fonts.googleapis.com/css2?family=Oswald:wght@500;600&family=Open+Sans:wght@400;600&family=Noto+Serif:ital@1&display=swap">
<style>
  :root {
    --brand-blue: #2a47b0;
    --brand-blue-deep: #132480;
    --light-gray: #dededd;
    --dark-gray: #6b7880;
    --ink: #2b2b2b;
    --paper: #ffffff;
    --stage: #2c2f33;
  }
  * { box-sizing: border-box; margin: 0; padding: 0; }
  html, body { width: 1200px; height: 900px; overflow: hidden; }
  body {
    background: var(--stage);
    display: flex; align-items: center; justify-content: center; gap: 60px;
    font-family: "Open Sans", sans-serif;
  }
  .card {
    position: relative; width: 520px; height: 298px;
    border-radius: 22px; overflow: hidden;
    box-shadow: 0 18px 40px rgba(0,0,0,.45);
  }

  /* Front */
  .card--front { background: var(--paper); color: var(--ink); }
  .front__identity { position: absolute; left: 34px; top: 30px; width: 250px; }
  .front__name {
    font-family: "Oswald", sans-serif; font-weight: 600; font-size: 24px;
    letter-spacing: .5px; line-height: 1;
  }
  .front__title {
    font-family: "Noto Serif", serif; font-style: italic; font-size: 12px;
    color: var(--brand-blue); margin-top: 4px;
  }
  .front__divider { height: 1px; background: var(--light-gray); margin-top: 10px; width: 250px; }
  .front__phones { position: absolute; left: 34px; top: 112px; list-style: none; }
  .front__phones li {
    display: flex; align-items: center; gap: 8px;
    font-size: 11.5px; line-height: 20px; color: #444;
  }
  .icon { width: 11px; height: 11px; fill: var(--brand-blue); flex: none; }

  .front__logo-box {
    position: absolute; right: 34px; top: 32px; width: 176px; height: 100px;
    background: var(--brand-blue); display: flex; align-items: center; justify-content: center;
    padding: 6px;
  }
  .front__logo-box span {
    display: flex; width: 100%; height: 100%; align-items: center; justify-content: center;
    border: 1.5px solid var(--light-gray);
    font-family: "Oswald", sans-serif; font-weight: 500; font-size: 18px; color: var(--paper);
    letter-spacing: .5px; white-space: nowrap;
  }
  .front__accent { position: absolute; right: 34px; top: 148px; width: 176px; height: 3px; background: var(--brand-blue); }
  .front__address {
    position: absolute; right: 34px; top: 160px; list-style: none; text-align: right;
  }
  .front__address li {
    display: flex; justify-content: flex-end; align-items: flex-start; gap: 8px;
    font-size: 11.5px; line-height: 17px; color: #333; margin-bottom: 3px;
  }
  .front__address .icon { margin-top: 3px; }

  .front__band {
    position: absolute; left: 0; right: 0; bottom: 0; height: 36px;
    background: var(--brand-blue); display: flex; align-items: center; justify-content: center;
    color: var(--paper); font-size: 12px; letter-spacing: .3px;
  }

  /* Back */
  .card--back {
    background: radial-gradient(ellipse at 60% 35%, #3553c2 0%, var(--brand-blue) 55%, #2440a6 100%);
    color: var(--paper);
    display: flex; flex-direction: column; align-items: center; justify-content: center;
  }
  .back__wordmark {
    font-family: "Oswald", sans-serif; font-weight: 500; font-size: 38px; letter-spacing: 1px;
    display: flex; align-items: center; gap: 14px; white-space: nowrap;
  }
  .back__mark { width: 22px; height: 22px; background: var(--light-gray); flex: none; }
  .back__rule { width: 300px; height: 1.5px; background: var(--light-gray); margin: 14px 0 12px; }
  .back__slogan {
    font-family: "Oswald", sans-serif; font-weight: 600; font-size: 14px;
    letter-spacing: .8px; text-transform: uppercase;
  }
</style>
</head>
<body>

<section class="card card--front" aria-label="Business card front">
  <div class="front__identity">
    <h1 class="front__name">YOUR NAME</h1>
    <p class="front__title">Job Title</p>
    <div class="front__divider"></div>
  </div>

  <ul class="front__phones">
    <li><svg class="icon" viewBox="0 0 12 12"><rect x="1" y="4" width="10" height="7" rx="1"/><rect x="2" y="1" width="8" height="2.5" rx="1"/></svg>000 000 0000</li>
    <li><svg class="icon" viewBox="0 0 12 12"><rect x="3" y="0.5" width="6" height="11" rx="1.2"/></svg>000 000 0000</li>
    <li><svg class="icon" viewBox="0 0 12 12"><rect x="1" y="5" width="10" height="6" rx="1"/><rect x="3" y="1" width="6" height="4"/></svg>000 000 0000</li>
  </ul>

  <div class="front__logo-box"><span>Belford &amp; Company</span></div>
  <div class="front__accent"></div>

  <ul class="front__address">
    <li><span>0000, Anywehre, Somewhere<br>City. ST 0000</span>
      <svg class="icon" viewBox="0 0 12 12"><path d="M6 0.5a4 4 0 0 1 4 4c0 3-4 7-4 7s-4-4-4-7a4 4 0 0 1 4-4zm0 2.3a1.7 1.7 0 1 0 0 3.4 1.7 1.7 0 0 0 0-3.4z"/></svg></li>
    <li><span>youremail@xyz.com</span>
      <svg class="icon" viewBox="0 0 12 12"><path d="M0.5 2.5h11v7h-11z M0.5 2.5l5.5 4 5.5-4" stroke="#fff" stroke-width=".8"/></svg></li>
  </ul>

  <footer class="front__band">www.belfordandcompany.example</footer>
</section>

<section class="card card--back" aria-label="Business card back">
  <div class="back__wordmark"><span class="back__mark"></span>Belford &amp; Company</div>
  <div class="back__rule"></div>
  <p class="back__slogan">Precision Guides Every Step</p>
</section>

</body>
</html>
```